Empower our Electric Journey on the Web

We need a new website that can promote our services. Our three services that we offer are:
- Management of e-mobility charging stations
- Management of energy purchases
- Leasing of E-Mobility charging stations
- Energy billing of private electricity meters
The website should work responsively on PC, tablet and smartphone. In general, a simple navigation and an appealing design should be in the foreground. The website should give the customer the possibility to request , based pm a preset chexkbox chart and to get in contact with us.
Our logo works on black and white background.
Our slogan is:
Empower Your Electric Journey with Velnik Mobility
The 4 Pages should be the following:
Main Page, with info about us, why choose us,
2nd; services; what we sell and what are our services
3rd; Contact us, request an offer
4th, References about costumers and Work we already did, in the future we would like to integrate a Blog Post in this section in stead of references.

Target Market(s)

Landlords, Homeowners, Homeowner Associations

Industry/Entity Type

EV Chargers / E-Mobility

Coding

Coded - Design and coding required

Number of Pages Required

4 page

Requirements
Nice to have
• Pop up to our mailchimp newsletter subscription

```html
<!DOCTYPE html>
<html lang="en">
<head>
<meta charset="utf-8">
<title>Velnik Mobility – Smart Electric Car Charging</title>
<link href="https://fonts.googleapis.com/css2?family=Orbitron:wght@700;800&family=Roboto:wght@400;500;700&display=swap" rel="stylesheet">
<style>
:root{
  --green:#4ec22f;
  --green-bright:#62d63a;
  --green-dark:#2f8f1c;
  --ink:#111111;
  --ink-soft:#444444;
  --dark:#151816;
  --white:#ffffff;
  --muted:#9aa19b;
}
*{box-sizing:border-box;margin:0;padding:0}
html,body{width:1200px;height:4898px;overflow:hidden}
body{font-family:"Roboto",Arial,sans-serif;color:var(--ink);background:var(--white)}
.page{position:relative;width:1200px;height:4898px;overflow:hidden}
section,header,footer{position:absolute;left:0;width:1200px;overflow:hidden}
.abs{position:absolute}
.display{font-family:"Orbitron","Arial Black",sans-serif;font-weight:800;letter-spacing:1.5px;text-transform:uppercase}
.eyebrow{font-size:13px;font-weight:700;color:var(--green);letter-spacing:.6px;text-transform:uppercase}
.center{left:0;width:1200px;text-align:center}
.lead{font-size:14px;line-height:23px;color:var(--ink-soft)}
.btn{position:absolute;display:flex;align-items:center;justify-content:center;background:var(--green);color:var(--white);font-size:13px;font-weight:700;text-transform:uppercase;letter-spacing:.4px}
.ghost-word{position:absolute;left:0;width:1200px;text-align:center;font-family:"Orbitron",sans-serif;font-weight:800;font-size:76px;letter-spacing:2px;color:rgba(78,194,47,.08);white-space:nowrap;text-transform:uppercase}

/* nav */
.site-nav{top:0;height:52px;background:var(--white);border-bottom:1px solid #e6e6e6}
.brand{display:flex;align-items:center;gap:8px;font-family:"Orbitron",sans-serif;font-weight:800;font-size:16px;letter-spacing:1px;text-transform:uppercase}
.brand-dot{width:14px;height:14px;border-radius:50%;background:var(--green)}
.nav-link{position:absolute;top:19px;font-size:12px;font-weight:500;letter-spacing:1px;color:#222}
.nav-link.active{color:var(--green)}

/* hero */
.hero{top:52px;height:568px;background:linear-gradient(100deg,#0d1a0c 0%,#1f3319 40%,#3d4a3a 70%,#6c7a6b 100%)}
.hero-photo{position:absolute;inset:0;background:radial-gradient(circle at 83% 40%,rgba(120,255,120,.35),transparent 25%),linear-gradient(180deg,rgba(0,0,0,0) 60%,rgba(0,0,0,.35))}
.hero h1{position:absolute;left:122px;top:165px;color:var(--white);font-size:35px;line-height:45px}
.hero p{position:absolute;left:122px;top:310px;width:470px;color:#e8ece8;font-size:11px;line-height:19px}

/* services */
.services{top:620px;height:725px;background:linear-gradient(180deg,#fff 0%,#fff 55%,#eef0ee 100%)}
.section-title{position:absolute;font-size:29px;line-height:45px;color:var(--ink)}
.service-card{position:absolute;top:240px;width:224px;height:357px}
.service-photo{position:absolute;left:0;top:0;width:224px;height:333px}
.service-body{position:absolute;left:22px;right:22px;top:205px;bottom:0;background:var(--white);box-shadow:0 4px 14px rgba(0,0,0,.12);text-align:center;padding:0 10px}
.service-icon{position:absolute;left:50%;top:-48px;transform:translateX(-50%);width:96px;height:96px;border-radius:50%;background:var(--green);border:5px solid var(--white);display:flex;align-items:center;justify-content:center}
.service-body h3{font-size:12px;font-weight:500;line-height:19px;margin-top:60px}
.service-body p{font-size:9.5px;line-height:14px;color:#777;margin-top:4px}
.more{font-size:10.5px;font-weight:500;margin-top:6px;display:block}

/* about */
.about{top:1345px;height:528px;background:linear-gradient(90deg,#2a2d2a 0%,#121412 55%,#0c0d0c 100%)}
.about-photo{position:absolute;left:0;top:0;width:640px;height:528px;background:linear-gradient(100deg,#4a4e49 0%,#2c302b 55%,rgba(18,20,18,0) 100%)}
.about h2{position:absolute;left:668px;top:112px;color:var(--white);font-size:29px;line-height:45px}
.about p{position:absolute;left:668px;top:262px;width:420px;color:#d8dcd8;font-size:11px;line-height:19px}

/* features */
.features{top:1873px;height:666px;background:var(--white)}
.feature{position:absolute;width:250px}
.feature h4{font-size:13.5px;font-weight:500;margin-bottom:5px}
.feature p{font-size:10px;line-height:19px;color:#555}
.feature-icon{position:absolute;width:64px;height:64px;border-radius:50%;background:var(--green);box-shadow:0 0 0 5px rgba(78,194,47,.18);display:flex;align-items:center;justify-content:center}

/* blog */
.blog{top:2539px;height:651px;background:linear-gradient(120deg,#1a1d1a,#2a2f2a 50%,#1c1f1c)}
.post{position:absolute;top:213px;width:253px}
.post-photo{width:253px;height:187px}
.post-meta{margin-top:18px;font-size:8px;color:#cfd3cf;display:flex;gap:14px;align-items:center;text-transform:uppercase}
.post-meta i{display:inline-block;width:9px;height:9px;border-radius:50%;background:var(--green);margin-right:4px;vertical-align:-1px}
.post h3{font-size:14px;font-weight:400;color:var(--white);line-height:19px;margin-top:8px}
.post p{font-size:9.5px;line-height:19px;color:#cfd3cf;margin-top:8px}
.post .read{display:block;margin-top:14px;font-size:10px;color:var(--green)}

/* stations */
.stations{top:3190px;height:658px;background:var(--white)}
.stat{position:absolute;left:122px;display:flex;gap:10px;align-items:flex-start}
.stat strong{display:block;font-size:27px;line-height:28px;font-weight:700;color:var(--green)}
.stat span{font-size:11px;line-height:14px;color:#333}
.map-area{position:absolute;left:380px;top:262px;width:733px;height:358px;background:linear-gradient(135deg,#eaf7e4 0%,#bfe8ad 50%,#e6f5de 100%)}

/* how */
.how{top:3848px;height:521px;background:linear-gradient(180deg,#1b1e1b,#232823 60%,#1b1e1b)}
.step-num{position:absolute;width:68px;height:68px;border-radius:50%;border:4px solid var(--green);background:#1b1e1b;color:var(--white);font-family:"Orbitron",sans-serif;font-weight:800;font-size:26px;display:flex;align-items:center;justify-content:center}
.step{position:absolute;width:220px;text-align:center}
.step h4{font-size:17px;font-weight:500;color:var(--green)}
.step p{font-size:10px;line-height:19px;color:#d6dad6;margin-top:12px}

/* cta */
.cta{top:4369px;height:266px;background:linear-gradient(100deg,#3fb22a,#5ccf34 50%,#7ee04f)}
.cta h2{font-size:35px;color:var(--white)}
.cta .phone{font-family:"Orbitron",sans-serif;font-weight:700;font-size:23px;color:var(--white);letter-spacing:2px}

/* footer */
.site-footer{top:4635px;height:263px;background:#0e0f0e;color:var(--white)}
.foot-head{position:absolute;top:50px;font-family:"Orbitron",sans-serif;font-weight:700;font-size:17px;letter-spacing:1px}
.foot-list{position:absolute;top:82px;list-style:none;font-size:10.5px;text-transform:uppercase}
.foot-list li{height:23.8px;display:flex;align-items:center;gap:8px}
.social-dot{width:20px;height:20px;border-radius:50%;background:var(--green)}
.field{position:absolute;left:842px;width:246px;height:34px;background:var(--white);color:#555;font-size:11px;padding-left:12px;display:flex;align-items:center}
.copyright{position:absolute;left:0;top:232px;width:1200px;height:31px;border-top:1px solid #2a2a2a;text-align:center;font-size:11px;line-height:28px;color:#d8d8d8}
</style>
</head>
<body>
<div class="page">

<header class="site-nav">
  <div class="abs brand" style="left:122px;top:14px"><span class="brand-dot"></span>Velnik Mobility</div>
  <a class="nav-link active" style="left:371px">HOME</a>
  <a class="nav-link" style="left:456px">PAGES</a>
  <a class="nav-link" style="left:544px">SERVICES</a>
  <a class="nav-link" style="left:658px">FEARURES</a>
  <a class="nav-link" style="left:784px">BLOG</a>
  <a class="btn" style="left:987px;top:11px;width:91px;height:29px;font-size:10px">Contact Us</a>
</header>

<section class="hero">
  <div class="hero-photo" role="img" aria-label="Close-up photo of a charging cable plugged into an electric car with a glowing green connector"></div>
  <div class="ghost-word" style="top:440px">Velnik Mobility</div>
  <div class="abs eyebrow" style="left:122px;top:132px;font-size:12px">Welcome to Velnik Mobility</div>
  <h1 class="display">Feture Solutions<br>for Smart Electric<br>Car Charging</h1>
  <p>Lorem Ipsum is simply dummy text of the printing and typesetting industry. Lorem Ipsum has been the industry's standard dummy text ever since the 1500s, when an unknown printer took a galley of type and scrambled it to make a type specimen book.</p>
  <a class="btn" style="left:122px;top:382px;width:152px;height:40px">Get Started</a>
</section>

<section class="services">
  <div class="abs eyebrow center" style="top:60px">Our Services</div>
  <h2 class="display section-title center" style="top:88px">Convenient and<br>reliable solutions for<br>smart electric car charging</h2>

  <div class="service-card" style="left:122px">
    <div class="service-photo" role="img" aria-label="Photo of a green electric car charger" style="background:linear-gradient(160deg,#8fd46c,#5aa83e 60%,#c9d9c0)"></div>
    <div class="service-body" style="top:175px">
      <div class="service-icon"><svg width="44" height="44" viewBox="0 0 44 44" fill="none" stroke="#fff" stroke-width="2.5"><rect x="10" y="8" width="18" height="28" rx="2"/><path d="M28 16h4v14a3 3 0 0 0 6 0V18"/><path d="M20 14l-4 8h6l-4 8"/></svg></div>
      <h3>Management of<br>e-mobility charging stations</h3>
      <p>Lorem Ipsum is simply dummy text of the printing and typesetting industry. Lorem Ipsum has been the industry's standard dummy text</p>
      <span class="more">Learn More ⟶</span>
    </div>
  </div>
  <div class="service-card" style="left:365px">
    <div class="service-photo" role="img" aria-label="Photo of a hand holding a charging plug" style="background:linear-gradient(160deg,#d9dcd8,#9aa09a 50%,#5a4a40)"></div>
    <div class="service-body">
      <div class="service-icon"><svg width="44" height="44" viewBox="0 0 44 44" fill="none" stroke="#fff" stroke-width="2.5"><rect x="8" y="10" width="20" height="24" rx="2"/><path d="M28 18h6v10"/><circle cx="34" cy="31" r="3"/><path d="M14 18h8M14 24h8"/></svg></div>
      <h3>Management of energy<br>purchases</h3>
      <span class="more" style="margin-top:8px">Learn More ⟶</span>
    </div>
  </div>
  <div class="service-card" style="left:609px">
    <div class="service-photo" role="img" aria-label="Photo of an electric car connected to a charging station" style="background:linear-gradient(160deg,#c9d0d6,#7f8a94 55%,#3a4248)"></div>
    <div class="service-body">
      <div class="service-icon"><svg width="44" height="44" viewBox="0 0 44 44" fill="none" stroke="#fff" stroke-width="2.5"><path d="M8 28l3-9h22l3 9v5H8z"/><circle cx="14" cy="33" r="3"/><circle cx="30" cy="33" r="3"/><path d="M22 8l-3 6h5l-3 6"/></svg></div>
      <h3>Leasing of E-Mobility<br>charging stations</h3>
      <span class="more" style="margin-top:8px">Learn More ⟶</span>
    </div>
  </div>
  <div class="service-card" style="left:852px">
    <div class="service-photo" role="img" aria-label="Photo of a charging plug inserted in a white car" style="background:linear-gradient(160deg,#e4e6e4,#a7aca7 55%,#2f2f2f)"></div>
    <div class="service-body">
      <div class="service-icon"><svg width="44" height="44" viewBox="0 0 44 44" fill="none" stroke="#fff" stroke-width="2.5"><circle cx="22" cy="22" r="14"/><path d="M24 12l-7 11h6l-3 9 8-12h-6z"/></svg></div>
      <h3>Energy billing of private<br>electricity meters</h3>
      <span class="more" style="margin-top:8px">Learn More ⟶</span>
    </div>
  </div>
  <a class="btn" style="left:512px;top:645px;width:175px;height:40px">View All Services</a>
</section>

<section class="about">
  <div class="about-photo" role="img" aria-label="Photo of a hand plugging a charger into an electric car, framed in angular green-outlined panels"></div>
  <div class="ghost-word" style="top:400px">Velnik Mobility</div>
  <div class="abs eyebrow" style="left:668px;top:80px">About Us</div>
  <h2 class="display">Modern cities<br>electric vehicle<br>charging stations</h2>
  <p>Lorem Ipsum is simply dummy text of the printing and typesetting industry. Lorem Ipsum has been the industry's standard dummy text ever since the 1500s, when an unknown printer took a galley of type and scrambled it to make a type specimen book. It has survived not only five centuries, but also the leap into electronic typesetting, remaining essentially unchanged.</p>
  <a class="btn" style="left:668px;top:384px;width:175px;height:40px">Learn More</a>
</section>

<section class="features">
  <div class="abs eyebrow center" style="top:50px;text-transform:none;font-size:14px">Our Features</div>
  <h2 class="display section-title center" style="top:68px">Velnik Mobility Features</h2>
  <p class="abs lead center" style="top:120px">Lorem Ipsum is simply dummy text of the printing and typesetting industry. Lorem Ipsum<br>has been the industry's standard dummy text ever since the 1500s</p>

  <div class="feature" style="left:106px;top:262px;text-align:right"><h4>High Quality</h4><p>Lorem Ipsum is simply<br>dummy text of the printing</p></div>
  <div class="feature" style="left:106px;top:382px;text-align:right"><h4>Fast DC Charging</h4><p>Lorem Ipsum is simply<br>dummy text of the printing</p></div>
  <div class="feature" style="left:106px;top:502px;text-align:right"><h4>Easy Process</h4><p>Lorem Ipsum is simply<br>dummy text of the printing</p></div>
  <div class="feature-icon" style="left:373px;top:249px"><svg width="32" height="32" viewBox="0 0 32 32" fill="none" stroke="#fff" stroke-width="2"><circle cx="16" cy="16" r="11"/><path d="M11 16l4 4 7-8"/></svg></div>
  <div class="feature-icon" style="left:373px;top:369px"><svg width="32" height="32" viewBox="0 0 32 32" fill="none" stroke="#fff" stroke-width="2"><path d="M12 5v6M20 5v6M9 11h14v6a7 7 0 0 1-14 0zM16 24v5"/></svg></div>
  <div class="feature-icon" style="left:373px;top:491px"><svg width="32" height="32" viewBox="0 0 32 32" fill="none" stroke="#fff" stroke-width="2"><circle cx="16" cy="16" r="11"/><circle cx="16" cy="16" r="4"/><path d="M16 5v4M16 23v4M5 16h4M23 16h4"/></svg></div>

  <div class="abs" role="img" aria-label="Photo of a white electric vehicle charging station with a coiled cable" style="left:520px;top:200px;width:160px;height:418px;background:linear-gradient(90deg,#dfe2df,#f6f7f6 45%,#d3d6d3)"></div>

  <div class="feature-icon" style="left:763px;top:249px"><svg width="32" height="32" viewBox="0 0 32 32" fill="none" stroke="#fff" stroke-width="2"><rect x="8" y="6" width="16" height="20" rx="2"/><path d="M17 10l-3 6h4l-3 6"/></svg></div>
  <div class="feature-icon" style="left:763px;top:369px"><svg width="32" height="32" viewBox="0 0 32 32" fill="none" stroke="#fff" stroke-width="2"><circle cx="16" cy="16" r="11"/><path d="M12 16h8M16 12v8"/></svg></div>
  <div class="feature-icon" style="left:763px;top:491px"><svg width="32" height="32" viewBox="0 0 32 32" fill="none" stroke="#fff" stroke-width="2"><circle cx="16" cy="16" r="11"/><path d="M17 9l-5 8h5l-2 6 6-9h-5z"/></svg></div>
  <div class="feature" style="left:846px;top:262px"><h4>Wall Mounted</h4><p>Lorem Ipsum is simply<br>dummy text of the printing</p></div>
  <div class="feature" style="left:846px;top:382px"><h4>Get Peace Mind</h4><p>Lorem Ipsum is simply<br>dummy text of the printing</p></div>
  <div class="feature" style="left:846px;top:502px"><h4>Onboard EFTPOS</h4><p>Lorem Ipsum is simply<br>dummy text of the printing</p></div>
</section>

<section class="blog">
  <div class="ghost-word" style="top:520px">Velnik Mobility</div>
  <div class="abs eyebrow center" style="top:56px">Recent Articles</div>
  <h2 class="display section-title center" style="top:82px;color:#fff">Our Latest Blog</h2>
  <p class="abs lead center" style="top:134px;color:#e0e4e0">Lorem Ipsum is simply dummy text of the printing and typesetting industry. Lorem Ipsum<br>has been the industry's standard dummy text ever since the 1500s</p>

  <article class="post" style="left:198px">
    <div class="post-photo" role="img" aria-label="Photo of a white car plugged into a charger" style="background:linear-gradient(160deg,#f0f0f0,#bfc2bf 60%,#3c3c3c)"></div>
    <div class="post-meta"><span><i></i>By Admin</span><span><i></i>0 Comments</span></div>
    <h3>EVs give maximum charging<br>speed</h3>
    <p>Lorem Ipsum is simply dummy text of the printing and typesetting industry. Lorem Ipsum has been the industry's standard dummy text ever since the</p>
    <span class="read">Read More ⟶</span>
  </article>
  <article class="post" style="left:468px">
    <div class="post-photo" role="img" aria-label="Photo of a woman holding a charging plug next to a car" style="background:linear-gradient(160deg,#d6dde2,#9fb0bd 55%,#5f6e78)"></div>
    <div class="post-meta"><span><i></i>By Admin</span><span><i></i>0 Comments</span></div>
    <h3>EVs give maximum charging<br>speed</h3>
    <p>Lorem Ipsum is simply dummy text of the printing and typesetting industry. Lorem Ipsum has been the industry's standard dummy text ever since the</p>
    <span class="read">Read More ⟶</span>
  </article>
  <article class="post" style="left:738px">
    <div class="post-photo" role="img" aria-label="Photo of a white car charging on a street" style="background:linear-gradient(160deg,#e6e8e6,#a9aea9 55%,#7a2a2a)"></div>
    <div class="post-meta"><span><i></i>By Admin</span><span><i></i>0 Comments</span></div>
    <h3>EVs give maximum charging<br>speed</h3>
    <p>Lorem Ipsum is simply dummy text of the printing and typesetting industry. Lorem Ipsum has been the industry's standard dummy text ever since the</p>
    <span class="read">Read More ⟶</span>
  </article>
</section>

<section class="stations">
  <div class="abs eyebrow center" style="top:60px">Recent Articles</div>
  <h2 class="display section-title center" style="top:84px;line-height:38px">More than 1500 charging<br>stations &amp; growing big!</h2>
  <p class="abs lead center" style="top:177px">Lorem Ipsum is simply dummy text of the printing and typesetting industry. Lorem Ipsum<br>has been the industry's standard dummy text ever since the 1500s</p>

  <div class="stat" style="top:330px"><svg width="36" height="40" viewBox="0 0 36 40" fill="none" stroke="#222" stroke-width="2"><path d="M18 36s-11-12-11-20a11 11 0 0 1 22 0c0 8-11 20-11 20z"/><circle cx="18" cy="16" r="4"/><ellipse cx="18" cy="37" rx="12" ry="2"/></svg><div><strong>300K</strong><span>Charging Ports<br>Worldwide</span></div></div>
  <div class="stat" style="top:436px"><svg width="36" height="40" viewBox="0 0 36 40" fill="none" stroke="#222" stroke-width="2"><rect x="6" y="4" width="18" height="32" rx="2"/><path d="M24 14h5v14a2.5 2.5 0 0 0 5 0V16"/><path d="M16 12l-4 8h6l-4 8"/></svg><div><strong>980K</strong><span>Electric Vehicle<br>Owners</span></div></div>
  <div class="stat" style="top:540px"><svg width="40" height="40" viewBox="0 0 40 40" fill="none" stroke="#222" stroke-width="2"><circle cx="20" cy="20" r="15"/><path d="M20 10v10l7 5"/><path d="M5 20H2M38 20h-3"/></svg><div><strong>99%</strong><span>Charging Station<br>Uptime</span></div></div>

  <div class="map-area" role="img" aria-label="Green world map showing charging station locations across all continents"></div>
</section>

<section class="how">
  <div class="ghost-word" style="top:420px">Velnik Mobility</div>
  <div class="abs eyebrow center" style="top:66px">How We Works</div>
  <h2 class="display section-title center" style="top:90px;line-height:38px;color:#fff">Professional EV Charging<br>Solution for you</h2>
  <p class="abs lead center" style="top:177px;color:#e0e4e0">Lorem Ipsum is simply dummy text of the printing and typesetting industry. Lorem Ipsum<br>has been the industry's standard dummy text ever since the 1500s</p>

  <svg class="abs" style="left:200px;top:240px" width="800" height="130" fill="none" stroke="#ffffff" stroke-width="2" stroke-dasharray="6 6">
    <path d="M14 80 C60 40,100 38,140 45"/>
    <path d="M210 45 C280 45,330 70,360 85"/>
    <path d="M430 85 C480 60,550 40,610 45"/>
    <path d="M680 45 C720 45,760 60,780 78"/>
  </svg>
  <div class="step-num" style="left:308px;top:251px">01</div>
  <div class="step-num" style="left:559px;top:293px">02</div>
  <div class="step-num" style="left:809px;top:251px">03</div>
  <div class="step" style="left:232px;top:341px"><h4>Our Network</h4><p>Lorem Ipsum is simply dummy text of<br>the printing and typesetting industry.</p></div>
  <div class="step" style="left:483px;top:381px"><h4>Charge Points</h4><p>Lorem Ipsum is simply dummy text of<br>the printing and typesetting industry.</p></div>
  <div class="step" style="left:733px;top:336px"><h4>EV Stations</h4><p>Lorem Ipsum is simply dummy text of<br>the printing and typesetting industry.</p></div>
</section>

<section class="cta">
  <h2 class="display abs center" style="top:56px">Safe &amp; easy to use charging</h2>
  <div class="abs phone center" style="top:120px">FEEL FREE TO CALL US:+(555) 013-2846</div>
  <a class="btn" style="left:493px;top:169px;width:173px;height:40px;background:#fff;color:#111">Contact Now</a>
</section>

<footer class="site-footer">
  <div class="abs brand" style="left:122px;top:52px;font-size:18px"><span class="brand-dot"></span>Velnik Mobility</div>
  <p class="abs" style="left:122px;top:96px;width:170px;font-size:10.5px;line-height:17px;color:#e0e0e0">Lorem Ipsum is simply dummy text of the printing and typesetting industry. Lorem Ipsum has been the industry's standard</p>

  <div class="foot-head" style="left:426px">Home</div>
  <ul class="foot-list" style="left:426px"><li>Home</li><li>Pages</li><li>Services</li><li>Fearures</li><li>Blog</li></ul>

  <div class="foot-head" style="left:612px">Follow us</div>
  <ul class="foot-list" style="left:612px"><li><span class="social-dot"></span>Friendbook</li><li><span class="social-dot"></span>ClipStream</li><li><span class="social-dot"></span>Chirpline</li><li><span class="social-dot"></span>Snapgallery</li></ul>

  <div class="foot-head" style="left:842px">Newsletter</div>
  <div class="field" style="top:84px">Email</div>
  <div class="field" style="top:128px">Address</div>
  <a class="btn" style="left:842px;top:173px;width:110px;height:33px;font-size:12px">Subscribe</a>

  <div class="copyright">Copyright © 2010-2023 velnik mobility. All rights reserved.</div>
</footer>

</div>
</body>
</html>
```